Stonefield Crafters Brochure = SCC $$$

this brochure will be used for a canvassing campaign (door to door) appointment setting

the campaign will be for homeowners that would like to do any kind of improvement to their house - home improvement
from EXT paint or roof repair all the way to kitchen and bathroom remodeling

we want to catch the prospect eye with the brochure and to educate our prospect about the different ways they could improve their house step by step to their dream house

Target Market(s)

Homeowners
anyone who would like to improve or fix any part of their house

Industry/Entity Type

Home Improvement

Contact Information for Business Card

the green roof house blueprints on one side
the Stonefield Crafters logo on the other side

Font styles to use
Serif
Decorative

Colors
ffffff
886aae
9bcb3b
e6e6e6

Requirements
Must have
• this is a TRI-FOLD brochure
• call for action -- schedule your free estimate
• or any idea that will lead to set up an appointment with our specialist
• LOOK AT MY WEBSITE TO UNDERSTAND MORE WHAT I LIKE
• WWW.STONEFIELDCRAFTERSCO.EXAMPLE
• services:
• Kitchen Renovations
• Bathroom Renovations
• Modern Landscaping
• Additions + in-law quarters
• Exterior paint +interior paint
• wood replacement + stucco repair
• roof repair
• railling and glass work
Nice to have
• the pictures I have uploaded can use as an example but im open to other ideas...
• THERE IS NO SUBSTITUTE FOR QUALITY.
• the picture of the women in the kitchen--
• i enjoy making food and spending time in my new kitchen, to see my whole family sitting down to eat dinner together in our perfect little kitchen make me so happy
Should not have
• the 2 brochures i have uploaded are for example only

```html
<!DOCTYPE html>
<html lang="en">
<head>
<meta charset="utf-8">
<title>Stonefield Crafters Tri-Fold Brochure</title>
<link href="https://fonts.googleapis.com/css2?family=Lato:wght@400;700;900&display=swap" rel="stylesheet">
<style>
  :root{
    --green:#8dc63f;
    --green-deep:#3f8a1f;
    --charcoal:#3a3a3a;
    --ink:#1f1f1f;
    --paper:#ffffff;
    --mist:#e6e6e6;
    --stage:#d9d9d9;
    --wall:#d4a22e;
  }
  *{box-sizing:border-box;margin:0;padding:0}
  html,body{width:1200px;height:800px;overflow:hidden}
  body{background:var(--stage);font-family:'Lato',Arial,sans-serif;color:var(--ink)}
  .brochure{position:absolute;left:60px;top:50px;width:1080px;height:700px;background:var(--paper);box-shadow:0 6px 20px rgba(0,0,0,.18);display:flex}
  .panel{position:relative;width:360px;height:700px;overflow:hidden}

  /* left panel */
  .panel--intro .swoosh{position:absolute;inset:0}
  .intro-copy{position:absolute;left:30px;top:70px;width:300px;color:var(--paper)}
  .intro-copy h1{font-weight:900;font-size:38px;line-height:1.02;letter-spacing:.5px;text-transform:uppercase}
  .intro-copy p{margin-top:16px;font-size:12.5px;line-height:1.55;font-weight:700}
  .about{position:absolute;left:30px;top:462px;width:300px}
  .about h2{color:var(--green-deep);font-weight:900;font-size:20px;line-height:1.05;text-transform:uppercase}
  .about p{margin-top:10px;font-size:11.5px;line-height:1.55;color:var(--ink)}
  .about .about-sign{margin-top:12px;font-weight:900}

  /* photo spread */
  .photo-spread{position:absolute;left:360px;top:0;width:720px;height:700px;
    background:
      linear-gradient(180deg,rgba(255,255,255,0) 55%,rgba(240,240,240,.85) 78%,rgba(238,238,238,.95) 100%),
      linear-gradient(90deg,var(--wall) 0%,#c99428 17%,#5a3d2a 21%,#6a4a34 24%,#e4e6e8 27%,#f2f2f2 45%,#cfcfcf 58%,#e9ecec 72%,#a8b79a 88%,#d6dcd2 100%)}
  .panel--contact,.panel--cover{background:transparent}
  .contact{position:absolute;left:30px;bottom:50px;width:300px}
  .brand{display:flex;align-items:center;gap:10px}
  .brand-dot{display:block;width:34px;height:34px;border-radius:50%;background:var(--green-deep);flex:none}
  .brand-name{font-weight:900;font-size:22px;letter-spacing:1px;text-transform:uppercase;color:var(--charcoal)}
  .phone{margin-top:14px;font-size:27px;font-weight:900;color:var(--ink)}
  .web{margin-top:6px;font-size:12px;color:var(--ink)}
  .address{margin-top:8px;font-size:12px;line-height:1.4;color:var(--ink)}

  .tab{position:absolute;left:100px;top:0;width:160px;height:130px}
  .tab-brand{position:absolute;left:100px;top:24px;width:160px;text-align:center}
  .tab-brand .brand-dot{margin:0 auto;width:30px;height:30px}
  .tab-brand .brand-name{display:block;margin-top:8px;font-size:13px;line-height:1.2;color:#7a7a7a;font-weight:700}

  .services{position:absolute;left:34px;top:160px;width:296px;padding:16px 18px;background:rgba(255,255,255,.82)}
  .services h3{font-weight:900;font-size:16px;text-transform:uppercase;color:var(--green-deep);letter-spacing:.5px}
  .services ul{margin-top:8px;list-style:none}
  .services li{position:relative;padding-left:16px;font-size:12.5px;line-height:1.7;font-weight:700;color:var(--ink)}
  .services li::before{content:"";position:absolute;left:0;top:7px;width:7px;height:7px;background:var(--green)}

  .slogan{position:absolute;left:34px;top:470px;width:300px;font-weight:900;font-size:31px;line-height:1.05;text-transform:uppercase;color:var(--ink)}
  .cta{position:absolute;left:34px;bottom:50px;width:296px;padding:12px 14px;background:var(--green-deep);color:var(--paper);text-align:center}
  .cta strong{display:block;font-weight:900;font-size:17px;text-transform:uppercase;letter-spacing:.5px}
  .cta span{display:block;margin-top:3px;font-size:12px;font-weight:700}
</style>
</head>
<body>
<main class="brochure">
  <div class="photo-spread" role="img" aria-label="Photo of a modern interior with a floating staircase, glass railing, yellow wall, kitchen and dining area"></div>

  <section class="panel panel--intro">
    <svg class="swoosh" width="360" height="700" viewBox="0 0 360 700" aria-hidden="true">
      <path d="M0 0H360V318C250 330 120 350 0 395Z" fill="var(--green)"/>
      <path d="M0 395C120 350 250 330 360 318V345C250 352 120 372 0 420Z" fill="var(--charcoal)"/>
      <path d="M0 420C120 372 250 352 360 345V370C250 372 120 392 0 448Z" fill="var(--mist)"/>
      <path d="M0 700V672C120 680 250 692 360 668V700Z" fill="var(--mist)" opacity=".6"/>
    </svg>
    <div class="intro-copy">
      <h1>Let's<br>change<br>your living.</h1>
      <p>Picture the perfect room. Everyone comes up with a different one: a cozy reading nook; a laser-filled bowling alley; a light-filled art studio. Ever wished you could bring your vision to reality? Tell us what you envision, and we'll help you bring it to life!</p>
    </div>
    <div class="about">
      <h2>About<br>Stonefield Crafters</h2>
      <p>We believe that every project deserves the same kind of attention, no matter if it's a one room remodel or a new build of a multimillion dollar structure. To us, quality is achieving the best results with the highest-grade material, at the lowest cost to you. That is how we define quality and that is what you're getting with Stonefield Crafters.</p>
      <p class="about-sign">We believe and live by our words...</p>
    </div>
  </section>

  <section class="panel panel--contact">
    <div class="contact">
      <div class="brand"><span class="brand-dot"></span><span class="brand-name">Stonefield Crafters</span></div>
      <p class="phone">(555) 318-2406</p>
      <p class="web">www.stonefieldcraftersco.example</p>
      <p class="address">417 Alder Crest Ave. Unit #2,<br>Fairview, CA 90000</p>
    </div>
  </section>

  <section class="panel panel--cover">
    <svg class="tab" width="160" height="130" viewBox="0 0 160 130" aria-hidden="true">
      <path d="M0 0H160V95L80 130L0 95Z" fill="#f1f0ec"/>
    </svg>
    <div class="tab-brand"><span class="brand-dot"></span><span class="brand-name">Stonefield Crafters</span></div>
    <div class="services">
      <h3>Our Services</h3>
      <ul>
        <li>Kitchen Renovations</li>
        <li>Bathroom Renovations</li>
        <li>Modern Landscaping</li>
        <li>Additions + In-Law Quarters</li>
        <li>Exterior + Interior Paint</li>
        <li>Wood Replacement + Stucco Repair</li>
        <li>Roof Repair</li>
        <li>Railing and Glass Work</li>
      </ul>
    </div>
    <p class="slogan">There is no<br>substitute<br>for quality.</p>
    <div class="cta">
      <strong>Schedule your free estimate</strong>
      <span>Call (555) 318-2406 to meet our specialist</span>
    </div>
  </section>
</main>
</body>
</html>
```